Craft a new attractive & professional PowerPoint presentation based on the material provided

Dear Designer,
We are looking for a fresh revamp of our Corporate Power Point presentation. Please find attached:
- the current ppt file;
- new pdf with Corporate profile;
- our logo.
For more information please consult our Social Media Channels:
LinkedIn: https://www.linkedin.com/company/7419063/admin/
IG: https://www.instagram.com/norvapaint/
YT: https://www.youtube.com/channel/UCqWm4TzRk8LpBnDe2VxHjaf
Deadline: before November 20th 2022.
Please do not hesitate to reach out for any questions.
Best wishes,
NRV Marketing Team
Font styles to use
Other font styles liked:
- Helvetica types
Colors
Designer to choose colors to be used in the design.
Look and feel
Each slider illustrates characteristics of the customer's brand and the style your logo design should communicate.

```html
<!DOCTYPE html>
<html lang="en">
<head>
<meta charset="utf-8">
<title>NRV Corporate Presentation</title>
<link href="https://fonts.googleapis.com/css2?family=Nunito+Sans:wght@400;600;800;900&display=swap" rel="stylesheet">
<style>
:root{
  --page:#a7adad;
  --red:#d6001c;
  --ink:#1f1f22;
  --white:#ffffff;
  --map:#4a4d52;
}
*{margin:0;padding:0;box-sizing:border-box}
html,body{width:1200px;height:3947px;overflow:hidden}
body{background:var(--page);font-family:"Nunito Sans",Helvetica,Arial,sans-serif;color:var(--ink);position:relative}
.slide{position:absolute;left:115px;width:1001px;height:563px;overflow:hidden;background:var(--white)}
.abs{position:absolute}
.brand{position:absolute;background:var(--red);color:var(--white);font-weight:900;display:flex;align-items:center;justify-content:center;border-radius:6px;letter-spacing:.5px}
.brand--on-red{outline:3px solid var(--white)}
.heading{font-weight:900;text-transform:uppercase;letter-spacing:.3px;white-space:nowrap}
.ruled{border-top:3px solid var(--red);border-bottom:3px solid var(--red);display:flex;align-items:center}

/* cover */
.cover{top:95px}
.cover__band{left:0;top:0;width:500px;height:563px;background:var(--red)}
.cover__photo{left:94px;top:52px;width:814px;height:458px;background:linear-gradient(120deg,#8e1620 0%,#b0101c 45%,#5b5b5e 75%,#9aa0a4 100%)}
.cover__caption{left:620px;top:401px;width:288px;height:109px;background:var(--white);color:var(--red);font-size:37px;line-height:40px;padding:14px 0 0 14px}

/* family */
.family{top:725px}
.family__head{left:192px;top:0;width:809px;height:175px;background:var(--red);color:var(--white);padding:42px 0 0 98px}
.family__head h2{font-size:31px;font-weight:800}
.family__head p{font-size:15px;line-height:19px;margin-top:10px}
.family__photo{left:0;top:175px;width:1001px;height:388px;background:linear-gradient(180deg,#c9d3da 0%,#b8a98a 38%,#6f7063 62%,#55575a 100%)}

/* key facts */
.facts{top:1356px;background:var(--red)}
.facts__top{left:0;top:0;width:1001px;height:150px;background:var(--white);border-bottom:8px solid var(--ink)}
.facts__title{left:484px;top:35px;height:72px;font-size:26px;font-weight:800;padding:0 2px}
.card{position:absolute;width:219px;height:193px;background:var(--white);border-radius:8px;padding:0 36px;display:flex;flex-direction:column;justify-content:center;font-size:15px;line-height:21px}
.card strong{color:var(--red);font-weight:800;font-size:24px;margin-top:16px}
.card strong small{font-size:16px}
.card b{font-weight:800;margin-top:16px}
.card b + strong{margin-top:10px}

/* world */
.world{top:1986px}
.world__title{left:158px;top:37px;width:483px;height:72px;font-size:24px;font-weight:800;letter-spacing:.2px}
.pill{position:absolute;left:48px;width:282px;height:90px;background:var(--red);color:var(--white);border-radius:8px;font-size:14px;font-weight:800;line-height:20px;padding:0 38px;display:flex;align-items:center}
.world__map{left:353px;top:175px;width:605px;height:306px;background:radial-gradient(ellipse at 50% 45%,#5a5d62 0%,#4a4d52 60%,rgba(74,77,82,0) 100%)}

/* italy */
.italy{top:2616px;background:linear-gradient(180deg,#e7ebee 0%,#d9dfe4 45%,#b9b3a2 62%,#6b6d6d 80%,#4e5153 100%)}
.italy__title{left:0;top:176px;width:1001px;text-align:center;font-size:26px;font-weight:800}
.italy__text{left:0;top:230px;width:1001px;text-align:center;font-size:16px;line-height:23px}

/* solutions */
.solutions{top:3248px;background:radial-gradient(ellipse at 55% 45%,#6f6a60 0%,#3a3631 55%,#1e1c1a 100%)}
.solutions__title{left:32px;top:461px;color:var(--white);font-size:30px;line-height:33px}
</style>
</head>
<body>

<section class="slide cover">
  <div class="abs cover__band"></div>
  <div class="abs cover__photo" role="img" aria-label="Worker in a red branded shirt and protective gloves holding a brush"></div>
  <div class="brand brand--on-red" style="left:858px;top:31px;width:80px;height:76px;font-size:27px">NRV</div>
  <div class="abs cover__caption heading">Your finish<br>partner</div>
</section>

<section class="slide family">
  <div class="brand" style="left:58px;top:48px;width:74px;height:74px;font-size:25px">NRV</div>
  <div class="abs family__head">
    <h2 class="heading">A family company</h2>
    <p>Driving excellence and keeping on developing innovative products<br>thanks to our incredible Team of Talents.</p>
  </div>
  <div class="abs family__photo" role="img" aria-label="Company team standing in front of the headquarters building"></div>
</section>

<section class="slide facts">
  <div class="abs facts__top"></div>
  <div class="brand" style="left:376px;top:35px;width:73px;height:72px;font-size:25px">NRV</div>
  <div class="abs facts__title heading ruled">Key facts</div>
  <div class="card" style="left:32px;top:235px">One of the oldest family owned businesses in Italy:<strong>110+ <small>years</small></strong></div>
  <div class="card" style="left:268px;top:287px">Leading player on the brush market<b>Turnover 2021, €:</b><strong>15,6 mln</strong></div>
  <div class="card" style="left:509px;top:235px">We drive excellence thanks to our team of talents in Italy, Romania &amp; Spain:<strong>115+ <small>talents</small></strong></div>
  <div class="card" style="left:745px;top:287px">We offer a wide range of solutions b2b &amp; b2c:<strong>2000+ SKUs</strong></div>
</section>

<section class="slide world">
  <div class="brand" style="left:48px;top:37px;width:73px;height:70px;font-size:25px">NRV</div>
  <div class="abs world__title heading ruled">Our journey around the world</div>
  <div class="pill" style="top:170px">Constantly growing<br>customer base: 5,000+</div>
  <div class="pill" style="top:284px">Our products are sold<br>in 75+ countries</div>
  <div class="pill" style="top:395px">2 production sites in EU<br>(Italy &amp; Romania)</div>
  <div class="abs world__map" role="img" aria-label="World map"></div>
</section>

<section class="slide italy" role="img" aria-label="Headquarters building under a cloudy sky">
  <div class="brand" style="left:464px;top:71px;width:73px;height:72px;font-size:25px">NRV</div>
  <h2 class="abs italy__title heading">Proudly made in Italy</h2>
  <p class="abs italy__text">Our HQ in Valmora, just outside Castelbrino covers over<br>11.000 square meters of production, warehouse and offices.</p>
</section>

<section class="slide solutions" role="img" aria-label="Open hands holding several wire wheel brushes">
  <div class="brand" style="left:26px;top:17px;width:74px;height:72px;font-size:25px">NRV</div>
  <h2 class="abs solutions__title heading">Our solutions to<br>meet your needs</h2>
</section>

</body>
</html>
```